Wellness Wordpress Blog Redesign

I am looking to redesign by wordpress blog - www.MarnieCollardActive.com. I would like to have a more personalized feel that resonates with my brand of Renewed Balance through fitness, nutrition, self care and self love. I'd like capabilities to do the following:

Ideally, I'd like to have the home page feature not only my latest blog posts or videos, but to also include a place to click to learn more about other facets of my business.

Ideally, I'd love to have a page layout of:

Home - main page to host key features of the brand & latest blog posts
About - Place to learn more about me and my brand
Blog -
Fitness - Host some videos and fitness tips and links to resources
Nutrition - Host some videos and recipes and links to resources
Self Care - Host some videos and self care tips and links to resources
Shop - Host a video (that can be changed of the product of the month) and links to other resources

Number of Pages Required

5+ page

Font styles to use
Serif
Decorative

Colors
85acd3
0393ce
00a990
6b449b
a64599
b8a6cd

Requirements
Must have
• Home - main page to host key features of the brand & latest blog posts
• About - Place to learn more about me and my brand
• Blog -
• Fitness - Host some videos and fitness tips and links to resources
• Nutrition - Host some videos and recipes and links to resources
• Self Care - Host some videos and self care tips and links to resources
• Shop - Host a video (that can be changed of the product of the month) and links to other resources
• Video / Mutlimedia capabilities
Nice to have
• Option to have a calendar of events widgets for people to sign up for events that I'm hosting

```html
<!DOCTYPE html>
<html lang="en">
<head>
<meta charset="utf-8">
<title>Marnie Collard – Training &amp; Coaching</title>
<link href="https://fonts.googleapis.com/css2?family=Nunito:wght@400;600;700;800;900&display=swap" rel="stylesheet">
<style>
:root{
  --purple:#6b2d7f;
  --purple-deep:#4f2a86;
  --magenta:#a6409b;
  --green:#0fa58a;
  --ink:#1a1a1a;
  --dark:#1e1e1e;
  --text:#333;
  --muted:#555;
  --white:#fff;
}
*{margin:0;padding:0;box-sizing:border-box}
html,body{width:1200px;height:4128px;overflow:hidden}
body{font-family:"Nunito",sans-serif;color:var(--text);background:var(--white);position:relative}
.abs{position:absolute}
.photo{position:absolute}

/* header */
.site-header{position:absolute;left:0;top:0;width:1200px;height:105px;background:var(--white)}
.brand{position:absolute;left:132px;top:16px;color:var(--purple);font-weight:800;font-size:42px;line-height:1}
.brand small{display:block;font-size:10px;letter-spacing:4px;font-weight:800;text-align:center;margin-top:5px}
.header-phone{position:absolute;left:648px;top:20px;color:var(--purple);font-weight:800;font-size:19px;display:flex;align-items:center;gap:7px;white-space:nowrap}
.search{position:absolute;left:894px;top:19px;width:203px;height:28px;border:1px solid #ccc;border-radius:14px;font-size:11px;color:#777;padding:6px 14px}
.search svg{position:absolute;right:10px;top:7px}
.main-nav{position:absolute;left:473px;top:66px;display:flex;gap:20px;font-size:14.5px;font-weight:800;color:var(--ink)}

/* hero */
.hero{position:absolute;left:0;top:105px;width:1200px;height:600px;background:radial-gradient(ellipse 45% 55% at 30% 55%,#5a5a5a,transparent 70%),radial-gradient(ellipse at 70% 40%,#3e3e3e,#161616 72%)}
.hero .photo{left:600px;top:0;width:520px;height:583px;background:radial-gradient(ellipse 22% 16% at 54% 18%,#9a6a55,transparent 70%),radial-gradient(ellipse 30% 22% at 52% 48%,#141414,transparent 75%),radial-gradient(ellipse 16% 18% at 72% 62%,#a87359,transparent 70%),radial-gradient(ellipse 14% 20% at 30% 70%,#9b6650,transparent 70%),linear-gradient(180deg,#3a3030,#1e1a1a)}
.hero h1{position:absolute;left:130px;top:168px;color:var(--white);font-size:40px;font-weight:900;line-height:1.25}
.hero p{position:absolute;left:130px;top:280px;width:520px;color:#e6e6e6;font-size:16px;line-height:1.55}
.btn{display:inline-block;font-weight:800;text-transform:uppercase;border-radius:4px}
.btn-book{position:absolute;left:130px;top:355px;background:var(--magenta);color:var(--white);font-size:14px;padding:11px 18px}
.dots{position:absolute;left:132px;top:425px;display:flex;gap:5px}
.dots span{width:12px;height:12px;border-radius:50%;border:2px solid #ccc}
.dots span.on{background:var(--magenta);border-color:var(--magenta)}

/* welcome */
.welcome{position:absolute;left:0;top:688px;width:1200px;height:504px}
.welcome .photo{left:0;top:18px;width:605px;height:486px;background:radial-gradient(ellipse 9% 40% at 52% 50%,#1d1d1d,transparent 80%),radial-gradient(ellipse 8% 14% at 52% 88%,#f07c82,transparent 80%),linear-gradient(90deg,#8f9a8c 0,#c9cfc6 15%,#6d8a4f 30%,#dfe3dc 45%,#eceae6 60%,#9a9a94 78%,#e6e6e2 100%)}
.welcome .eyebrow{position:absolute;left:636px;top:135px;color:var(--purple);font-size:32px;font-weight:900}
.welcome h2{position:absolute;left:636px;top:172px;color:var(--ink);font-size:48px;font-weight:900}
.welcome p{position:absolute;left:636px;top:252px;width:430px;font-size:13px;line-height:1.85;color:var(--text)}
.btn-outline{position:absolute;border:2px solid var(--ink);border-radius:18px;font-size:13px;font-weight:800;padding:6px 14px;color:var(--ink)}

/* feature video */
.feature{position:absolute;left:0;top:1192px;width:1200px;height:578px;background:var(--dark);overflow:hidden}
.feature h2{position:absolute;left:127px;top:128px;color:var(--white);font-size:38px;font-weight:900;line-height:1.35}
.feature h2 em{font-style:normal;color:var(--green)}
.feature p{position:absolute;left:127px;top:294px;width:440px;color:#ddd;font-size:13px;line-height:1.85}
.feature .btn-outline{left:127px;top:420px;border-color:#fff;color:#fff}
.video-frame{position:absolute;left:583px;top:123px;width:517px;height:353px;border:2px solid #ddd;padding:10px}
.video-frame .photo{position:relative;width:100%;height:100%;background:radial-gradient(ellipse 22% 30% at 30% 70%,#4b3a5a,transparent 75%),radial-gradient(ellipse 22% 30% at 70% 70%,#2a2a2a,transparent 75%),radial-gradient(ellipse 12% 12% at 40% 40%,#b88470,transparent 75%),radial-gradient(ellipse 12% 12% at 62% 40%,#c29a82,transparent 75%),linear-gradient(180deg,#6e6866 0,#4a4444 40%,#7a6c68 100%)}
.play{position:absolute;left:50%;top:50%;width:74px;height:74px;margin:-37px 0 0 -37px;border-radius:50%;background:var(--white)}

/* services */
.services{position:absolute;left:0;top:1770px;width:1200px;height:800px}
.services .photo{left:110px;top:100px;width:440px;height:700px;background:radial-gradient(ellipse 20% 8% at 50% 14%,#1a1a1a,transparent 80%),radial-gradient(ellipse 22% 8% at 48% 30%,#1a1a1a,transparent 80%),radial-gradient(ellipse 24% 16% at 48% 44%,#b07a5c,transparent 80%),radial-gradient(ellipse 28% 28% at 48% 80%,#3e3e3e,transparent 80%),linear-gradient(180deg,#fff,#f4f4f4)}
.services h2{position:absolute;left:572px;top:115px;font-size:32px;font-weight:900;color:var(--ink)}
.service{position:absolute;left:572px;width:520px;height:120px}
.service .icon{position:absolute;left:0;top:8px;width:96px;height:96px;border-radius:50%;background:var(--purple);border:5px solid #fff;box-shadow:0 0 0 4px var(--purple);display:flex;align-items:center;justify-content:center}
.service h3{position:absolute;left:122px;top:0;font-size:20px;font-weight:800;color:var(--ink)}
.service p{position:absolute;left:122px;top:32px;width:400px;font-size:13px;line-height:1.85}

/* events */
.events{position:absolute;left:0;top:2500px;width:1200px;height:618px;background:radial-gradient(ellipse 20% 25% at 85% 22%,#5a1c1c,transparent 80%),radial-gradient(ellipse at 50% 50%,#2e2a2a,#141212)}
.events h2{position:absolute;left:0;width:1200px;top:118px;text-align:center;color:var(--white);font-size:32px;font-weight:900}
.event-card{position:absolute;top:225px;width:292px;height:275px;background:var(--white)}
.event-card .photo{position:relative;height:184px}
.event-date{position:absolute;left:10px;top:160px;width:52px;height:52px;border-radius:50%;background:var(--green);color:#fff;border:3px solid #fff;font-size:9px;font-weight:800;text-align:center;line-height:1.1;padding-top:11px}
.event-card h3{position:absolute;left:72px;top:193px;font-size:12.5px;font-weight:800;color:var(--ink)}
.event-card p{position:absolute;left:72px;top:212px;width:205px;font-size:10.5px;line-height:1.55;color:var(--muted)}

/* signup */
.signup{position:absolute;left:0;top:3118px;width:1200px;height:500px}
.signup .photo{left:110px;top:110px;width:482px;height:320px;background:radial-gradient(ellipse 16% 20% at 28% 30%,#1f1f1f,transparent 80%),radial-gradient(ellipse 30% 16% at 46% 62%,#2a2a2a,transparent 80%),radial-gradient(ellipse 22% 8% at 72% 48%,#3a3a3a,transparent 80%),radial-gradient(ellipse 8% 8% at 90% 40%,#8a93a0,transparent 80%),linear-gradient(90deg,#fff,#f6f6f6 50%,#fff)}
.signup .brand{left:826px;top:98px}
.signup h2{position:absolute;left:693px;top:188px;font-size:36px;font-weight:900;color:var(--ink)}
.signup p{position:absolute;left:650px;top:243px;width:418px;text-align:right;font-size:13px;line-height:1.7}
.email-form{position:absolute;left:650px;top:316px;width:418px;height:40px;border:1px solid #bbb;border-radius:20px;font-size:12px;color:#555;padding:11px 18px}
.email-form span{position:absolute;right:-1px;top:-1px;height:40px;width:96px;border-radius:0 20px 20px 0;background:var(--purple);color:#fff;font-weight:800;font-size:14px;text-align:center;line-height:40px}

/* footer */
.site-footer{position:absolute;left:0;top:3611px;width:1200px;height:517px;background:linear-gradient(90deg,#a8338f,#6b2f8d 55%,#4f2a86)}
.site-footer .brand{left:132px;top:170px;color:var(--white)}
.social{position:absolute;left:172px;top:250px;display:flex;gap:8px}
.social span{width:32px;height:32px;border-radius:50%;border:2px solid #fff}
.site-footer h4{position:absolute;color:#fff;font-size:21px;font-weight:900}
.contact-list{position:absolute;left:462px;top:170px;color:#fff;font-size:13px;list-style:none}
.contact-list li{position:relative;padding-left:34px;margin-bottom:26px;line-height:1.45}
.contact-list svg{position:absolute;left:0;top:1px}
.quick-links{position:absolute;left:806px;top:170px;list-style:none;color:#fff;font-size:13px}
.quick-links li{position:relative;padding-left:24px;line-height:24.5px}
.quick-links li::before{content:"";position:absolute;left:2px;top:8px;width:9px;height:9px;border-radius:50%;background:#fff}
.copyright{position:absolute;left:0;width:1200px;top:450px;text-align:center;color:#fff;font-size:12.5px}
</style>
</head>
<body>

<header class="site-header">
  <div class="brand">Marnie Collard<small>TRAINING &amp; COACHING</small></div>
  <div class="header-phone">
    <svg width="18" height="18" viewBox="0 0 24 24"><path fill="#6b2d7f" d="M6.6 10.8a15 15 0 0 0 6.6 6.6l2.2-2.2a1 1 0 0 1 1-.25 11.4 11.4 0 0 0 3.6.57 1 1 0 0 1 1 1V20a1 1 0 0 1-1 1A17 17 0 0 1 3 4a1 1 0 0 1 1-1h3.5a1 1 0 0 1 1 1c0 1.25.2 2.45.57 3.57a1 1 0 0 1-.25 1z"/></svg>
    CALL (555) 210-4870
  </div>
  <div class="search">Search
    <svg width="12" height="12" viewBox="0 0 24 24"><circle cx="10" cy="10" r="7" fill="none" stroke="#333" stroke-width="3"/><path d="M15 15l6 6" stroke="#333" stroke-width="3"/></svg>
  </div>
  <nav class="main-nav"><span>HOME</span><span>ABOUT</span><span>BLOG</span><span>FITNESS</span><span>NUTRITION</span><span>SELFCARE</span><span>SHOP</span><span>CONTACT US</span></nav>
</header>

<section class="hero">
  <div class="photo" role="img" aria-label="Athlete in sportswear sprinting against a smoky dark backdrop"></div>
  <h1>MARNIE COLLARD<br>FITNESS &amp; HEALTH COACH</h1>
  <p>Sed ut perspiciatis unde omnis iste natus error sit voluptatem accusantium doloremque laudantium, totam rem</p>
  <span class="btn btn-book">Book an appointment</span>
  <div class="dots"><span class="on"></span><span></span><span></span><span></span></div>
</section>

<section class="welcome">
  <svg class="abs" style="left:0;top:-18px" width="1200" height="40" viewBox="0 0 1200 40" preserveAspectRatio="none"><path fill="#fff" d="M0 22 L40 14 L80 24 L130 10 L190 20 L240 12 L300 22 L360 8 L420 20 L480 12 L540 24 L600 10 L660 20 L720 12 L780 22 L840 8 L900 20 L960 14 L1020 24 L1080 10 L1140 20 L1200 12 L1200 40 L0 40Z"/></svg>
  <div class="photo" role="img" aria-label="Coach standing on a sunny outdoor walkway in workout clothes"></div>
  <div class="eyebrow">WELCOME TO</div>
  <h2>Marnie Collard</h2>
  <p>Sed ut perspiciatis unde omnis iste natus error sit voluptatem accusantium doloremque laudantium, totam rem aperiam, eaque ipsa quae ab illo inventore veritatis et quasi architecto beatae vitae dicta sunt explicabo. Nemo enim ipsam voluptatem quia voluptas si</p>
  <span class="btn-outline" style="left:636px;top:376px">READ MORE</span>
</section>

<section class="feature">
  <svg class="abs" style="left:0;top:0" width="1200" height="578" viewBox="0 0 1200 578"><path fill="#0fa58a" d="M750 0 H1200 V578 H1010 L1000 440 L1100 420 L1060 100 L760 40 Z"/></svg>
  <h2>MARNIE COLLARD<br><em>FITNESS &amp; HEALTH</em><br>COACH</h2>
  <p>Sed ut perspiciatis unde omnis iste natus error sit voluptatem accusantium doloremque laudantium, totam rem aperiam, eaque ipsa quae ab illo inventore veritatis et quasi architecto beatae vitae dicta sunt explicabo. Nemo enim ipsam voluptatem quia voluptas sit</p>
  <span class="btn-outline">READ MORE</span>
  <div class="video-frame">
    <div class="photo" role="img" aria-label="Video still of two women doing a partner ab exercise in a boxing gym">
      <div class="play"><svg width="74" height="74" viewBox="0 0 74 74"><path d="M30 24 L52 37 L30 50Z" fill="#111"/></svg></div>
    </div>
  </div>
</section>

<section class="services">
  <div class="photo" role="img" aria-label="Fit woman measuring her waist with a tape measure"></div>
  <h2>OUR SERVICES</h2>
  <div class="service" style="top:210px"><div class="icon">
    <svg width="50" height="50" viewBox="0 0 50 50" fill="none" stroke="#fff" stroke-width="2.5" stroke-linecap="round"><rect x="6" y="16" width="6" height="18" rx="1.5"/><rect x="38" y="16" width="6" height="18" rx="1.5"/><rect x="12" y="19" width="4" height="12" rx="1"/><rect x="34" y="19" width="4" height="12" rx="1"/><path d="M16 25 H34"/></svg>
  </div><h3>FITNESS</h3><p>Sed ut perspiciatis unde omnis iste natus error sit voluptatem accusantium doloremque laudantium, totam rem aperiam, eaque ipsa quae ab illo inventore veritatis et quasi architecto</p></div>
  <div class="service" style="top:352px"><div class="icon">
    <svg width="50" height="50" viewBox="0 0 50 50" fill="none" stroke="#fff" stroke-width="2.5" stroke-linecap="round" stroke-linejoin="round"><path d="M25 16 C18 11 9 14 9 24 C9 34 16 42 21 42 C23 42 24 41 25 41 C26 41 27 42 29 42 C34 42 41 34 41 24 C41 14 32 11 25 16Z"/><path d="M25 16 C25 12 27 9 30 7"/><path d="M27 12 C30 8 35 9 36 10 C34 13 30 14 27 12Z"/></svg>
  </div><h3>NUTRITION</h3><p>Sed ut perspiciatis unde omnis iste natus error sit voluptatem accusantium doloremque laudantium, totam rem aperiam, eaque ipsa quae ab illo inventore veritatis et quasi architecto</p></div>
  <div class="service" style="top:502px"><div class="icon">
    <svg width="50" height="50" viewBox="0 0 50 50" fill="none" stroke="#fff" stroke-width="2.5" stroke-linecap="round"><path d="M25 11 C26 20 30 24 39 25 C30 26 26 30 25 39 C24 30 20 26 11 25 C20 24 24 20 25 11Z"/><path d="M25 3 V7 M25 43 V47 M3 25 H7 M43 25 H47 M10 10 L13 13 M37 37 L40 40 M40 10 L37 13 M13 37 L10 40"/></svg>
  </div><h3>HEALTH COACH</h3><p>Sed ut perspiciatis unde omnis iste natus error sit voluptatem accusantium doloremque laudantium, totam rem aperiam, eaque ipsa quae ab illo inventore veritatis et quasi architecto</p></div>
</section>

<section class="events">
  <svg class="abs" style="left:0;top:0" width="1200" height="70" viewBox="0 0 1200 70"><path fill="#fff" d="M0 0 H1200 V70 L600 0 L0 70Z"/><path d="M0 70 L600 4 L1200 70" fill="none" stroke="#6b2d7f" stroke-width="8"/></svg>
  <h2>CALENDAR OF EVENTS</h2>
  <article class="event-card" style="left:135px">
    <div class="photo" role="img" aria-label="Group of smiling women after a workout" style="background:radial-gradient(ellipse 30% 40% at 25% 60%,#c9467e,transparent 80%),radial-gradient(ellipse 30% 40% at 75% 65%,#8a5a9a,transparent 80%),linear-gradient(135deg,#6b4a3c,#b58a72)"></div>
    <div class="event-date">APR 25<br>2018</div>
    <h3>Personal High Intensity Training</h3>
    <p>Sed ut perspiciatis unde omnis iste natus error sit voluptatem accusantium</p>
  </article>
  <article class="event-card" style="left:454px">
    <div class="photo" role="img" aria-label="Class doing plank exercises in a gym" style="background:radial-gradient(ellipse 50% 20% at 50% 75%,#3a3a3a,transparent 80%),linear-gradient(180deg,#d6d2cc,#9c948c)"></div>
    <div class="event-date">APR 25<br>2018</div>
    <h3>Personal High Intensity Training</h3>
    <p>Sed ut perspiciatis unde omnis iste natus error sit voluptatem accusantium</p>
  </article>
  <article class="event-card" style="left:773px">
    <div class="photo" role="img" aria-label="Outdoor wellness fair with people at a booth" style="background:radial-gradient(ellipse 18% 30% at 30% 65%,#e9eef0,transparent 80%),radial-gradient(ellipse 20% 40% at 75% 65%,#2a3a5a,transparent 80%),linear-gradient(180deg,#5f8f4a,#a9b58a)"></div>
    <div class="event-date">APR 25<br>2018</div>
    <h3>Personal High Intensity Training</h3>
    <p>Sed ut perspiciatis unde omnis iste natus error sit voluptatem accusantium</p>
  </article>
</section>

<section class="signup">
  <div class="photo" role="img" aria-label="Woman balancing in a V-sit core exercise"></div>
  <div class="brand">Marnie Collard<small>TRAINING &amp; COACHING</small></div>
  <h2>SIGN UP FOR EVENTS</h2>
  <p>Nemo enim ipsam voluptatem quia voluptas sit aspernatur aut odit aut fugit, sed quia consequuntur magni dolores eos qui ratione voluptatem</p>
  <div class="email-form">Email<span>SIGN UP</span></div>
</section>

<footer class="site-footer">
  <svg class="abs" style="left:0;top:-2px" width="1200" height="40" viewBox="0 0 1200 40" preserveAspectRatio="none"><path fill="#fff" d="M0 0 H1200 V16 L1140 26 L1080 12 L1020 24 L960 14 L900 28 L840 12 L780 22 L720 14 L660 26 L600 12 L540 22 L480 10 L420 26 L360 14 L300 24 L240 12 L180 26 L120 14 L60 24 L0 14Z"/></svg>
  <div class="brand">Marnie Collard<small>TRAINING &amp; COACHING</small></div>
  <div class="social"><span></span><span></span><span></span><span></span></div>
  <h4 style="left:462px;top:120px">CONTACT US</h4>
  <ul class="contact-list">
    <li><svg width="16" height="20" viewBox="0 0 16 20"><path d="M8 1a6 6 0 0 0-6 6c0 5 6 12 6 12s6-7 6-12a6 6 0 0 0-6-6z" fill="none" stroke="#fff" stroke-width="1.6"/><circle cx="8" cy="7" r="2" fill="#fff"/></svg>Marnie Collard<br>Harbor Lane Studio<br>18 Willow Court</li>
    <li><svg width="18" height="18" viewBox="0 0 24 24"><path fill="#fff" d="M6.6 10.8a15 15 0 0 0 6.6 6.6l2.2-2.2a1 1 0 0 1 1-.25 11.4 11.4 0 0 0 3.6.57 1 1 0 0 1 1 1V20a1 1 0 0 1-1 1A17 17 0 0 1 3 4a1 1 0 0 1 1-1h3.5a1 1 0 0 1 1 1c0 1.25.2 2.45.57 3.57a1 1 0 0 1-.25 1z"/></svg>Phone: (555) 318-0420</li>
    <li><svg width="18" height="18" viewBox="0 0 18 18"><rect x="1" y="5" width="16" height="10" fill="none" stroke="#fff" stroke-width="1.6"/><rect x="4" y="1" width="10" height="5" fill="#fff"/></svg>Fax: (555) 318-0421</li>
    <li><svg width="18" height="14" viewBox="0 0 18 14"><rect x="1" y="1" width="16" height="12" fill="none" stroke="#fff" stroke-width="1.6"/><path d="M1 1l8 7 8-7" fill="none" stroke="#fff" stroke-width="1.6"/></svg>Email: info@marniecollardactive.com</li>
  </ul>
  <h4 style="left:806px;top:120px">QUICK LINKS</h4>
  <ul class="quick-links"><li>Home</li><li>About</li><li>Blog</li><li>Fitness</li><li>Nutrition</li><li>Selfcare</li><li>Shop</li><li>Contact us</li></ul>
  <p class="copyright">(c) 2018 Marnie Collard | All Rights Reserved | Disclaimer</p>
</footer>

</body>
</html>
```